Design a large parking banner – mandatory ticket validation in the shop

Banner Size:
548 cm (width) x 154 cm (height)
Note: The banner will be placed in a metal frame at our parking lot entrance, fully visible to every incoming truck driver. The message must be easy to read from a distance.
Goal of the Banner:
To inform all truck drivers that they must validate their entry ticket inside the shop, even if they are parking for a short time.
The message must be displayed in multiple languages for international drivers.
Mandatory Content:
Main message – in multiple languages (clearly separated or stacked):
Dutch (NL): Vergeet je ticket niet te valideren in de shop – verplicht, ook bij kort parkeren!
French (FR): N'oubliez pas de valider votre ticket à la boutique – obligatoire, même pour un court arrêt !
English (EN): Don't forget to validate your entry ticket in the shop – mandatory, even for short stops!
German (DE): Vergessen Sie nicht, Ihr Einfahrticket im Shop zu entwerten – Pflicht, auch bei kurzem Parken!
Polish (PL): Nie zapomnij zatwierdzić biletu w sklepie – obowiązkowe, nawet przy krótkim postoju!
Romanian (RO): Nu uitați să validați biletul în magazin – obligatoriu, chiar și pentru opriri scurte!
You can include more languages if space allows, but these are essential.
Opening Hours Block (in one section below):
Shop Opening Hours
Mon – Fri: 05:30 – 22:00
Sat & Sun: 08:00 – 22:00
Style & Branding:
The design must match the visual identity of Haulport 41Ter
Please refer to the attached photos of existing parking signage for guidance on colors, typography, and layout style
Our logo (attached) must be clearly visible and professionally integrated
Feel free to use icons or pictograms to visually support the message (e.g., ticket, truck, arrow)
Readability is key – large, bold text and high contrast colors that are visible from a distance
Target Audience:
International truck drivers – people who need fast, clear communication. Not everyone speaks the local language, so visual clarity and multilingual messaging are critical.
File Requirements:
Print-ready file (PDF or EPS) – 300 dpi at 1:10 scale
Include 5 cm bleed on all sides
Provide open source files if possible (AI or PSD)

```html
<!DOCTYPE html>
<html lang="en">
<head>
<meta charset="utf-8">
<title>Haulport 41Ter – Parking Ticket Banner</title>
<link rel="stylesheet" href="https://fonts.googleapis.com/css2?family=Montserrat:wght@300;400;600;700&family=Oswald:wght@600&display=swap">
<style>
  :root {
    --navy: #1c2147;
    --blue: #1a7fc4;
    --red: #d2202f;
    --white: #ffffff;
    --ink: #1c1f24;
    --page: #eeeeee;
  }
  * { box-sizing: border-box; margin: 0; padding: 0; }
  html, body { width: 1200px; height: 758px; overflow: hidden; background: var(--page); }
  body { font-family: "Montserrat", sans-serif; color: var(--white); }

  .banner {
    position: absolute; left: 0; top: 210px;
    width: 1200px; height: 337px; overflow: hidden;
    background: var(--white);
  }
  .banner-shapes { position: absolute; inset: 0; }

  .shop-photo {
    position: absolute; left: 830px; top: 0; width: 370px; height: 337px;
    background: linear-gradient(180deg, #d9d4cc 0%, #c9b9a3 22%, #8e8ea0 45%, #b88a62 65%, #e8e6e2 100%);
  }

  .headline { position: absolute; left: 24px; top: 26px; }
  .headline-kicker { font-weight: 600; font-size: 21px; letter-spacing: .3px; }
  .headline-main { font-weight: 600; font-size: 43px; line-height: 1.05; margin-top: 4px; }
  .mark { background: var(--blue); padding: 0 6px; }

  .hours { position: absolute; left: 24px; top: 226px; }
  .hours-title { font-weight: 700; font-size: 17px; line-height: 1.15; }
  .hours-title .flag { background: var(--red); padding: 0 5px; font-weight: 600; }
  .hours-list { list-style: none; font-weight: 300; font-size: 17px; line-height: 1.3; margin-top: 8px; }

  .notice { position: absolute; left: 440px; top: 22px; width: 420px; }
  .notice-title { font-weight: 700; font-size: 21px; margin-bottom: 10px; }
  .notice-title .mark { font-weight: 600; }
  .languages { list-style: none; }
  .language {
    display: flex; gap: 12px; align-items: center;
    font-weight: 300; font-size: 12.5px; line-height: 1.3; height: 41px;
  }
  .language-hash { font-size: 24px; font-weight: 300; width: 18px; flex: none; }

  .parking-sign {
    position: absolute; left: 958px; top: 22px; width: 222px; height: 56px;
    background: var(--ink); display: flex; align-items: center;
  }
  .parking-sign-p {
    width: 52px; height: 56px; background: var(--blue); flex: none;
    font-family: "Oswald", sans-serif; font-size: 36px; display: flex; align-items: center; justify-content: center;
  }
  .parking-sign-text {
    font-family: "Oswald", sans-serif; font-size: 17px; line-height: 1; padding-left: 12px; flex: 1; letter-spacing: .5px;
  }
  .parking-sign-arrow { margin-right: 12px; }

  .brand {
    position: absolute; left: 960px; top: 236px;
    display: flex; align-items: center; gap: 10px;
  }
  .brand-square { width: 18px; height: 18px; background: var(--navy); }
  .brand-name { font-weight: 700; font-size: 30px; color: var(--navy); }
</style>
</head>
<body>
  <section class="banner">
    <div class="shop-photo" role="img" aria-label="Photo of the shop interior with stocked shelves"></div>

    <svg class="banner-shapes" width="1200" height="337" viewBox="0 0 1200 337" aria-hidden="true">
      <polygon points="0,0 830,0 1000,168 830,337 0,337" fill="#1c2147"/>
      <polyline points="810,0 982,168 812,337" fill="none" stroke="#d2202f" stroke-width="2"/>
      <polygon points="0,138 455,337 0,337" fill="#1a7fc4"/>
    </svg>

    <div class="headline">
      <p class="headline-kicker">SHORT STOP OR LONG STAY</p>
      <p class="headline-main"><span class="mark">TICKET MUST</span> BE<br>VALIDATED<br>IN THE SHOP.</p>
    </div>

    <div class="hours">
      <p class="hours-title">SHOP <span class="flag">OPENING</span><br>HOURS.</p>
      <ul class="hours-list">
        <li>Mon – Fri: 05:30 – 22:00</li>
        <li>Sat &amp; Sun: 08:00 – 22:00</li>
      </ul>
    </div>

    <div class="notice">
      <p class="notice-title">PLEASE <span class="mark">REVIEW CAREFULLY</span></p>
      <ul class="languages">
        <li class="language"><span class="language-hash">#</span><span>English (EN): Don't forget to validate your entry ticket in the shop – mandatory, even for short stops!</span></li>
        <li class="language"><span class="language-hash">#</span><span>French (FR): N'oubliez pas de valider votre ticket à la boutique – obligatoire, même pour un court arrêt !</span></li>
        <li class="language"><span class="language-hash">#</span><span>Dutch (NL): Vergeet je ticket niet te valideren in de shop – verplicht, ook bij kort parkeren!</span></li>
        <li class="language"><span class="language-hash">#</span><span>German (DE): Vergessen Sie nicht, Ihr Einfahrticket im Shop zu entwerten – Pflicht, auch bei kurzem Parken!</span></li>
        <li class="language"><span class="language-hash">#</span><span>Polish (PL): Nie zapomnij zatwierdzić biletu w sklepie – obowiązkowe, nawet przy krótkim postoju!</span></li>
        <li class="language"><span class="language-hash">#</span><span>Romanian (RO): Nu uitați să validați biletul în magazin – obligatoriu, chiar și pentru opriri scurte!</span></li>
      </ul>
    </div>

    <div class="parking-sign">
      <span class="parking-sign-p">P</span>
      <span class="parking-sign-text">PARKING<br>ZONE</span>
      <svg class="parking-sign-arrow" width="18" height="18" viewBox="0 0 18 18" aria-hidden="true">
        <path d="M3 3 L15 15 M15 6 V15 H6" fill="none" stroke="#ffffff" stroke-width="3"/>
      </svg>
    </div>

    <div class="brand">
      <span class="brand-square"></span>
      <span class="brand-name">Haulport 41Ter</span>
    </div>
  </section>
</body>
</html>
```